Business Card Design Project

We have recently completed MakerHive projects for a new logo and wesbite.
We now require new business cards.
We hand out very little printed material to clients as all information is online. When we do hand out something, like a business card, we want it to have real impact and make a statement about the quality and professionalism of our company.
We have an idea of what we want our card to look like but we want a designer to make sure they have impact and look great.
Our requirements are…
Size: 85mm X 55mm - Landscape
Front of card: Logo plus the following contact information.
Derek Fenwick
Operations Manager
Phone +44(0) 1632 xxx xxx
Mobile +44(0) 7700 xxx xxx
Email derekf@corebitsys.example
Address 19 Tarlow Street, Aberdeen AB12 4QP
Website www.corebitsys.example
How you layout the front of the card is up to you, we would like to see some different ideas. Attached are two versions of our logo that may be used.
Back of card: We would like this to be simple but again have impact. Our current thought is to have the logo or just the large W design from the logo in white against a dark background, perhaps made up from the dark green in the logo.
The logos are attached so you can see the colours in them but the dark ones are..
Dark Blue = C:88, M:55, Y:44, K:28
Dark Green = C:87, M:53, Y:50, K:50
We sometimes also use a bright orange as an accent or highlight colour…
Orange: = C:0, M:39, Y:94, K:0

```html
<!DOCTYPE html>
<html lang="en">
<head>
<meta charset="utf-8">
<title>Corebit Systems — Business Cards</title>
<link rel="stylesheet" href="https://fonts.googleapis.com/css2?family=Open+Sans:wght@400;700&display=swap">
<style>
  :root {
    --backdrop: #2b2b2b;
    --teal-dark: #0f4049;
    --teal-logo: #124a55;
    --orange: #f5a31a;
    --white: #ffffff;
    --text-light: #e8eef0;
  }
  * { box-sizing: border-box; margin: 0; padding: 0; }
  html, body {
    width: 1200px; height: 900px; overflow: hidden;
    background: var(--backdrop);
    font-family: "Open Sans", sans-serif;
  }
  .stage { position: relative; width: 1200px; height: 900px; }
  .card {
    position: absolute; top: 292px;
    width: 485px; height: 315px;
    border-radius: 24px; overflow: hidden;
    box-shadow: 0 6px 14px rgba(0,0,0,.45);
  }
  .card--back { left: 100px; background: var(--teal-dark); }
  .card--front { left: 615px; background: var(--white); }

  .wordmark {
    position: absolute; font-weight: 700; letter-spacing: .04em;
    text-transform: uppercase; white-space: nowrap;
  }
  .card--back .wordmark {
    left: 0; right: 0; top: 132px; text-align: center;
    color: var(--white); font-size: 38px;
  }
  .card--front .wordmark {
    left: 80px; top: 62px; color: var(--teal-logo); font-size: 30px;
    display: flex; align-items: center; gap: 14px;
  }
  .wordmark__dot {
    width: 34px; height: 34px; border-radius: 50%; background: var(--teal-logo);
  }
  .front-shape { position: absolute; left: 0; top: 0; width: 485px; height: 315px; }

  .person { position: absolute; left: 30px; top: 226px; }
  .person__name { color: var(--orange); font-size: 21px; line-height: 1.15; }
  .person__role { color: var(--white); font-size: 15px; margin-top: 3px; }

  .contact {
    position: absolute; left: 237px; top: 214px; list-style: none;
    color: var(--text-light); font-size: 11.8px; line-height: 15.5px;
  }
  .contact li { display: flex; align-items: center; gap: 7px; white-space: nowrap; }
  .contact svg { width: 11px; height: 11px; flex: none; fill: var(--orange); }
</style>
</head>
<body>
<main class="stage">
  <section class="card card--back" aria-label="Card back">
    <div class="wordmark">Corebit Systems</div>
  </section>

  <section class="card card--front" aria-label="Card front">
    <svg class="front-shape" viewBox="0 0 485 315" aria-hidden="true">
      <path d="M0,172 Q240,174 485,158 L485,166 Q240,181 0,178 Z" fill="var(--orange)"/>
      <path d="M0,181 Q240,184 485,169 L485,315 L0,315 Z" fill="var(--teal-dark)"/>
    </svg>

    <div class="wordmark"><span class="wordmark__dot"></span>Corebit Systems</div>

    <div class="person">
      <p class="person__name">Derek Fenwick</p>
      <p class="person__role">Operations Manager</p>
    </div>

    <ul class="contact">
      <li><svg viewBox="0 0 12 12"><path d="M6 0a4 4 0 0 0-4 4c0 3 4 8 4 8s4-5 4-8a4 4 0 0 0-4-4zm0 5.5A1.5 1.5 0 1 1 6 2.5a1.5 1.5 0 0 1 0 3z"/></svg>19 Tarlow Street, Aberdeen AB12 4QP</li>
      <li><svg viewBox="0 0 12 12"><path d="M2.5 0.5l2 2.5-1.2 1.3c.8 1.7 2.2 3.1 3.9 3.9L8.5 7l2.5 2-1 2.5C5 11 1 7 0.5 1.5z"/></svg>+44(0) 1632 xxx xxx</li>
      <li><svg viewBox="0 0 12 12"><path d="M3 0h6v12H3zM4 1.5v8h4v-8z"/></svg>+44(0) 7700 xxx xxx</li>
      <li><svg viewBox="0 0 12 12"><path d="M0 2h12v1.2L6 7 0 3.2zM0 4.5l6 3.8 6-3.8V10H0z"/></svg>derekf@corebitsys.example</li>
      <li><svg viewBox="0 0 12 12"><path d="M6 0a6 6 0 1 0 0 12A6 6 0 0 0 6 0zm0 1.2c.7.8 1.2 2.2 1.3 4.2H4.7c.1-2 .6-3.4 1.3-4.2zM1.3 6.6h2.4c.1 1.6.4 2.9.9 3.8A4.8 4.8 0 0 1 1.3 6.6zm0-1.2a4.8 4.8 0 0 1 3.3-3.8c-.5.9-.8 2.2-.9 3.8zm3.4 1.2h2.6c-.1 2-.6 3.4-1.3 4.2-.7-.8-1.2-2.2-1.3-4.2zm3.6 0h2.4a4.8 4.8 0 0 1-3.3 3.8c.5-.9.8-2.2.9-3.8zm0-1.2c-.1-1.6-.4-2.9-.9-3.8a4.8 4.8 0 0 1 3.3 3.8z"/></svg>www.corebitsys.example</li>
    </ul>
  </section>
</main>
</body>
</html>
```